International Student Travel Company needs a web page re-designed

Pellham Journeys is a worldwide leader in student educational and performing arts travel programs. We provide high-quality tours that exceed the expectations of our participants/customers and enhance a student's learning experiences. Our mission is to forever change how every student sees the world around them. Our company has 3 distinct brands: Pellham Journeys (www.pellhamjourneys.example), Brightwell Voyages (www.brightwellvoyages.example) and Northfield Heritage Trips & Band Jamborees (www.nfheri.example).

As part of our travel programs, we offer participants the option to purchase travel insurance. We are looking to re-design the page that offers each participant the option to buy insurance during their online registration process to maximize the number of customers who purchase the recommended option. The registration process is set up behind a password protected registration website.

Here is a link to view the current page for each brand:
https://accounts.pellhamjourneys.example/tech/demo/3172
https://accounts.brightwellvoyages.example/tech/demo/3172
https://accounts.nfheri.example/tech/demo/3172

We are attaching the HTML for the current page so you can start with the current format that this design is a part of- for example, the header & footer and the "Registration Step # section".

Please note that this current design was created for the "Brightwell Voyages" brand as you may note the use of the orange color on the page. We would like to design the page so that we can easily implement the same design for all 3 brands. As you will see from looking at the brands online, they all share a similar blue that can be used where we need a color as you will see on our SAMPLE mock-up that we have included as an attachment.

In our SAMPLE mock-up (file attached named "SAMPLE webpage mock-up.pdf") we have icons at the top of the insurance option which is meant to be a link to a PDF that is an advertisement for each type of travel insurance. So, however you decide to design that element, please make sure to include that as a link that will open a PDF in a new tab. The "None" option will open up the PDF attached named "Note to Parents.pdf". The "Student Deluxe" option will open up the PDF attached named "Marlow & Pike.pdf". The "Student Deluxe with CFAR" option will open up the PDF attached named "CFAR.pdf".

The sample mock-up is just a sample draft idea of how we would want it to look. Please feel free to re-design completely or as close to this design as you wish using your best design judgment. The goal is to make it look very professional and convince customers to select the recommended "Student Deluxe with CFAR" option as this will fully protect them in case they need to cancel.

It is very important to use all the copy as its presented since the language has all been approved by the insurance company's compliance team.

*VERY IMPORTANT*
Please design this so that it is MOBILE friendly. Many of our customers register for our trips on their mobile devices. So, because we are presenting 3 options to compare we need to make sure the design works well on small mobile screens. So, please present your designs for both large computer screens and small mobile devices so we can see how it would look at the various different screen sizes.

Please let us know if you have any questions or require any more info from us to get started. We are looking forward to seeing your designs!

-Pellham Journeys Marketing Team

```html
<!DOCTYPE html>
<html lang="en">
<head>
<meta charset="utf-8">
<title>Pellham Journeys – Registration Step 5/8 – Travel Protection</title>
<link href="https://fonts.googleapis.com/css2?family=Arimo:wght@400;700&family=Roboto:wght@500;700&display=swap" rel="stylesheet">
<style>
:root{
  --navy:#0b2f8f;
  --band:#0d53d4;
  --heading:#0a3aa0;
  --red:#d8262f;
  --yellow:#ffb900;
  --footer:#0a6bb4;
  --ink:#222;
  --muted:#666;
  --panel:#f3f4f8;
  --line:#e2e4ea;
  --white:#fff;
}
*{box-sizing:border-box;margin:0;padding:0}
html,body{width:728px;height:1200px;overflow:hidden;background:var(--white)}
body{font-family:"Arimo",Arial,sans-serif;color:var(--ink)}
.canvas{position:relative;width:728px;height:1200px;overflow:hidden;background:var(--white)}
.abs{position:absolute}
.view-title{position:absolute;font-family:"Roboto",Arial,sans-serif;font-weight:700;font-size:15px;color:#000}

/* shared */
.brand{position:absolute;display:flex;align-items:center;gap:3px}
.brand-mark{border-radius:50%;background:var(--red)}
.brand-name{font-family:"Arimo",Arial,sans-serif;font-weight:400;color:var(--heading);white-space:nowrap}
.photo{position:absolute;background:linear-gradient(180deg,#9cc6ea 0%,#c9def0 45%,#7fa36a 78%,#4f7a44 100%)}
.hero-band{position:absolute;background:var(--band);display:flex;align-items:center;color:var(--white)}
.partner{display:flex;align-items:center;gap:2px;color:var(--white);font-weight:700;white-space:nowrap}
.partner-square{background:var(--white)}
.hero-copy{font-weight:700;text-transform:uppercase;font-style:normal}
.protect-title{position:absolute;font-family:"Roboto",Arial,sans-serif;font-weight:700;color:var(--heading)}
.copy{position:absolute;color:var(--ink)}
.copy p+p{margin-top:1em}
.trip-cost{position:absolute;color:var(--red);font-family:"Roboto",Arial,sans-serif;font-weight:500}
.reg-head{position:absolute;display:flex;justify-content:space-between;font-family:"Roboto",Arial,sans-serif;font-weight:500;color:#222}
.reg-head .step-num{color:var(--red)}
.tour-info{position:absolute;border:1px solid var(--line);background:var(--white)}
.tour-info-head{background:#f2f2f2;border-bottom:1px solid var(--line);color:#333}
.tour-info dl{color:var(--muted)}
.tour-info dd{display:inline;color:#333;font-weight:700}

/* plan cards */
.plan-band{position:absolute;background:var(--band)}
.plan{position:absolute;background:var(--navy);color:var(--white);text-align:center}
.plan-title{font-family:"Roboto",Arial,sans-serif;font-weight:700}
.plan-price{font-family:"Roboto",Arial,sans-serif;font-weight:700}
.plan-price sup{font-size:50%;font-weight:400}
.plan-tag{font-weight:700}
.plan-list{list-style:none;text-align:left}
.plan-list li{position:relative}
.plan-list li::before{position:absolute;left:0;top:0}
.plan-list .yes::before{content:"✓";color:var(--white)}
.plan-list .no{color:var(--red)}
.plan-list .no::before{content:"✕";color:var(--red)}
.ribbon{position:absolute;background:var(--red);color:var(--white);text-align:center}
.pdf-link{position:absolute;border-radius:50%;background:var(--band);border:1px solid var(--white);display:flex;align-items:center;justify-content:center;text-decoration:none}
.pdf-link span{color:var(--white);font-weight:700;border:0.5px solid var(--white);border-radius:1px;line-height:1}
.select-btn{position:absolute;background:var(--navy);color:var(--white);border-radius:999px;font-family:"Roboto",Arial,sans-serif;font-weight:700;display:flex;align-items:center;justify-content:center;border:1px solid var(--band);text-decoration:none}

/* benefit table */
.benefits{position:absolute}
.b-row{display:flex;align-items:center;border-bottom:1px solid var(--line);overflow:hidden}
.b-head{background:var(--panel);font-family:"Roboto",Arial,sans-serif;font-weight:700;color:#222}
.b-label{font-weight:700;color:#222}
.b-val{color:#444;white-space:nowrap}
.x-mark{color:var(--red);font-size:5.4px;line-height:1}
.tick{color:var(--heading);font-weight:700;line-height:1}

.notes{position:absolute;color:#444}
.notes p+p{margin-top:1em}
.limits-btn{position:absolute;background:var(--band);color:var(--white);border-radius:999px;display:flex;align-items:center;justify-content:center;text-decoration:none}
.site-footer{position:absolute;background:var(--footer);color:var(--white);font-family:"Roboto",Arial,sans-serif;font-weight:700}
.seal{background:var(--white);border:1px solid #c9d6c2;display:flex;align-items:center;gap:2px;padding:1px}
.seal i{display:block;background:#6aa84f}
.seal b{display:block;background:#dfe8da}

/* desktop specifics */
.covid-bar{position:absolute;left:0;top:68px;width:524px;height:18px;background:var(--yellow);font-size:5.3px;font-weight:700;display:flex;align-items:center;justify-content:center}
.signed-in{position:absolute;left:331px;top:96px;font-size:4.4px;color:#555}
.signed-in a{color:var(--red);margin-left:3px;text-decoration:none}
.header-rule{position:absolute;left:0;top:113px;width:524px;height:1px;background:#eee}
.desk-panel{position:absolute;left:96px;top:126px;width:220px;height:424px;background:var(--panel)}
.feedback-tab{position:absolute;left:0;top:194px;width:8px;height:62px;background:#2e8fe0;border:1px solid #b8d6f2;border-left:0;color:var(--white);font-size:3.6px;font-weight:700;writing-mode:vertical-rl;transform:rotate(180deg);display:flex;align-items:center;justify-content:center}
.d-plan .plan-title{font-size:5px;line-height:6.2px}
.d-plan .plan-price{font-size:6.8px;margin-top:3px}
.d-plan .plan-tag{font-size:3.8px;line-height:5.4px;margin:7px 4px 0}
.d-plan .plan-list{font-size:3.5px;line-height:5.2px;margin:8px 2px 0 3px}
.d-plan .plan-list li{padding-left:5px;margin-bottom:4px}
.d-plan .select-btn{font-size:4.8px;height:12px;width:44px}
.d-table .b-label{font-size:3.9px;line-height:5.4px;width:74px;padding-left:1px}
.d-table .b-none{width:30px;text-align:center}
.d-table .b-dlx{width:58px;font-size:4px;padding-left:2px}
.d-table .b-cfar{width:58px;font-size:4px;padding-left:2px}
.d-table .b-head{font-size:4.2px}

/* mobile specifics */
.m-plan .plan-title{font-size:6.8px;line-height:8px}
.m-plan .plan-price{font-size:6.3px;margin-top:2px}
.m-plan .plan-tag{font-size:3.8px;line-height:5.4px;margin:6px 4px 0}
.m-plan .plan-list{font-size:3.5px;line-height:5.2px;margin:5px 2px 0 5px}
.m-plan .plan-list li{padding-left:6px;margin-bottom:4px}
.m-plan .select-btn{font-size:4.8px;height:11px;width:45px}
.m-table .b-label{font-size:3.4px;line-height:5px;width:58px;padding-left:2px}
.m-table .b-none{width:14px;text-align:center}
.m-table .b-dlx{width:29px;font-size:3.7px;padding-left:3px}
.m-table .b-head{font-size:3.6px}
.m-table .x-mark{font-size:5px}
.menu-btn{position:absolute;left:643px;top:76px;width:13px;height:11px;background:var(--navy);display:flex;flex-direction:column;justify-content:center;gap:1.6px;padding:0 3px}
.menu-btn span{display:block;height:0.8px;background:var(--white)}
.scroll-hint{position:absolute;left:585px;top:964px;width:40px;height:1.5px;border-radius:1px;background:#333}
</style>
</head>
<body>
<div class="canvas">

  <!-- ================= DESKTOP ================= -->
  <div class="view-title" style="left:185px;top:40px">Desktop View</div>
  <div class="covid-bar">For Coronavirus (COVID-19) Updates Please Click Here</div>

  <div class="brand" style="left:98px;top:92px">
    <span class="brand-mark" style="width:14px;height:14px"></span>
    <span class="brand-name" style="font-size:9px">Pellham Journeys</span>
  </div>
  <div class="signed-in">signed on as webuser@mail.example <a href="#">[Logout]</a></div>
  <div class="header-rule"></div>
  <div class="feedback-tab">Questions? Comments?</div>

  <div class="desk-panel"></div>
  <div class="photo" role="img" aria-label="Photo of smiling students taking a selfie in front of the Eiffel Tower" style="left:96px;top:126px;width:220px;height:116px"></div>
  <div class="hero-band" style="left:100px;top:242px;width:211px;height:30px">
    <div class="partner" style="width:60px;height:30px;justify-content:center;background:#1a5fe0;font-size:3.8px">
      <span class="partner-square" style="width:7px;height:7px"></span>HARBORLINE
    </div>
    <div class="hero-copy" style="font-size:4.9px;line-height:6.2px;padding-left:6px;width:150px">Travel insurance is optional, but unexpected events are always a possibility… and without the Student Deluxe Group Travel Protection, you might lose up to 100% of your trip investment</div>
  </div>

  <div class="protect-title" style="left:100px;top:282px;font-size:8.2px">PROTECT YOUR TRIP INVESTMENT!</div>
  <div class="copy" style="left:100px;top:298px;width:210px;font-size:4.5px;line-height:6.8px">
    <p>Harborline Travel Cover, a leading provider of group travel insurance, offers participants the opportunity to protect their travel investment.</p>
    <p>This program offers an array of <b>travel protection</b> benefits including 24/7 Worldwide Non-Insurance Assistance Services as well as Trip Cancellation, Trip Interruption, Medical Expense, Baggage and Personal Effects, and more travel insurance coverages such as the Cancel for Any Reason (CFAR) option, if eligible.</p>
  </div>
  <div class="trip-cost" style="left:103px;top:355px;font-size:6.4px">To start, please enter your total Trip Cost: $______</div>

  <div class="plan-band" style="left:96px;top:504px;width:220px;height:45px"></div>

  <div class="plan d-plan" style="left:100px;top:382px;width:68px;height:148px">
    <div class="plan-title" style="margin-top:9px">NONE</div>
    <div class="plan-price"><sup>$</sup>0</div>
    <div class="plan-tag">Potentially lose 100% of your tour cost</div>
    <ul class="plan-list" style="margin-top:8px"><li class="no">No Payment Protection</li></ul>
    <a class="select-btn" href="#" style="left:12px;top:145px">SELECT</a>
  </div>
  <div class="plan d-plan" style="left:172px;top:382px;width:68px;height:148px">
    <div class="plan-title" style="margin-top:9px">STUDENT DELUXE</div>
    <div class="plan-price"><sup>$</sup>100</div>
    <div class="plan-tag">Protects your trip investment for covered reasons only</div>
    <ul class="plan-list">
      <li class="yes">Trip Cancellation coverage provides a 100% refund if you need to cancel for covered reasons</li>
      <li class="yes">Includes additional coverages as per below Schedule</li>
      <li class="no">Does NOT include Cancel for Any Reason (CFAR)***</li>
      <li class="no">No coverage for cancellations due to fear of a pandemic</li>
    </ul>
    <a class="select-btn" href="#" style="left:11px;top:144px">SELECT</a>
  </div>
  <div class="ribbon" style="left:243px;top:373px;width:68px;height:9px;font-size:4.2px;line-height:9px">RECOMMENDED</div>
  <div class="plan d-plan" style="left:243px;top:382px;width:68px;height:148px">
    <div class="plan-title" style="margin-top:9px">STUDENT DELUXE<br>WITH CFAR</div>
    <div class="plan-price"><sup>$</sup>150</div>
    <div class="plan-tag" style="margin-top:4px">Protects your trip investment if you need to cancel for any reason***</div>
    <ul class="plan-list" style="margin-top:5px">
      <li class="yes">Trip Cancellation coverage provides a 100% refund if you need to cancel for covered reasons</li>
      <li class="yes">Includes additional coverages as per below Schedule</li>
      <li class="yes">Includes Cancel for Any Reason (CFAR)***</li>
      <li class="yes">Covers cancellation due to fear of a pandemic ***</li>
    </ul>
    <a class="select-btn" href="#" style="left:13px;top:144px">SELECT</a>
  </div>
  <a class="pdf-link" href="#" target="_blank" style="left:99px;top:372px;width:12px;height:12px"><span style="font-size:2.6px;padding:0.6px">PDF</span></a>
  <a class="pdf-link" href="#" target="_blank" style="left:170px;top:372px;width:12px;height:12px"><span style="font-size:2.6px;padding:0.6px">PDF</span></a>
  <a class="pdf-link" href="#" target="_blank" style="left:241px;top:372px;width:12px;height:12px"><span style="font-size:2.6px;padding:0.6px">PDF</span></a>

  <div class="benefits d-table" style="left:96px;top:554px;width:220px">
    <div class="b-row b-head" style="height:18px"><span style="width:74px;font-size:6.8px;padding-left:4px;font-weight:500">Benefit</span><span class="b-none" style="font-size:4.2px">NONE</span><span class="b-dlx">STUDENT DELUXE</span><span class="b-cfar">STUDENT DELUXE WITH CFAR</span></div>
    <div class="b-row" style="height:15px"><span class="b-label">CANCEL FOR ANY REASON (CFAR)***</span><span class="b-none x-mark">✕</span><span class="b-dlx x-mark">✕</span><span class="b-cfar tick" style="padding-left:4px;font-size:6.4px">✓</span></div>
    <div class="b-row" style="height:14px"><span class="b-label">Trip Cancellation**</span><span class="b-none x-mark">✕</span><span class="b-dlx b-val">Trip Cost*</span><span class="b-cfar b-val">Trip Cost*</span></div>
    <div class="b-row" style="height:13px"><span class="b-label">Trip Interruption**</span><span class="b-none x-mark">✕</span><span class="b-dlx b-val">150% Trip Cost</span><span class="b-cfar b-val">150% Trip Cost</span></div>
    <div class="b-row" style="height:13px"><span class="b-label">Travel Delay – 6 Hours</span><span class="b-none x-mark">✕</span><span class="b-dlx b-val">$750 ($150/day)</span><span class="b-cfar b-val">$750 ($150/day)</span></div>
    <div class="b-row" style="height:18px"><span class="b-label">Missed Connection –<br>3 Hours</span><span class="b-none x-mark">✕</span><span class="b-dlx b-val">$500</span><span class="b-cfar b-val">$500</span></div>
    <div class="b-row" style="height:14px"><span class="b-label">Baggage/Personal Effects</span><span class="b-none x-mark">✕</span><span class="b-dlx b-val">$1,500</span><span class="b-cfar b-val">$1,500</span></div>
    <div class="b-row" style="height:12px"><span class="b-label">Baggage Delay – 24 Hours</span><span class="b-none x-mark">✕</span><span class="b-dlx b-val">$300</span><span class="b-cfar b-val">$300</span></div>
    <div class="b-row" style="height:22px"><span class="b-label">Emergency Medical Evacuation, Medical Repatriation &amp; Return of Remains</span><span class="b-none x-mark">✕</span><span class="b-dlx b-val">$100,000</span><span class="b-cfar b-val">$100,000</span></div>
    <div class="b-row" style="height:17px"><span class="b-label">Accident &amp; Sickness Medical Expense</span><span class="b-none x-mark">✕</span><span class="b-dlx b-val">$25,000</span><span class="b-cfar b-val">$25,000</span></div>
    <div class="b-row" style="height:17px"><span class="b-label">Non-Medical Emergency Evacuation</span><span class="b-none x-mark">✕</span><span class="b-dlx b-val">$100,000</span><span class="b-cfar b-val">$100,000</span></div>
    <div class="b-row" style="height:17px"><span class="b-label">Non-Insurance Worldwide Emergency Assistance Services</span><span class="b-none x-mark">✕</span><span class="b-dlx b-val">Included</span><span class="b-cfar b-val">Included</span></div>
  </div>

  <div class="notes" style="left:96px;top:757px;width:220px;font-size:3.6px;line-height:5.3px">
    <p>Coverages may vary and not all coverage is available in all jurisdictions. Totals listed below each coverage are the maximum benefit amount payable.</p>
    <p>* Up to the lesser of the Trip Cost paid or the limit of Coverage for which benefits are requested and the appropriate plan cost has been paid. Maximum limit of $10,000</p>
    <p>** For $0 Trip Cost, there is no Trip Cancellation and Trip Interruption is limited to $500 return air only</p>
    <p>*** CFAR coverage is the lessor of 75% of the nonrefundable trip cost or up to the maximum of $10,000. CFAR is optional and available for purchase on an individual level. Trip cancellation must be 48 hours or more prior to scheduled departure. CFAR must be purchased at the time of plan purchase and with, or before your final payment. CFAR is available if you paid your Travel Supplier for the full cost for all non-refundable trip costs for your trip prior to your cancellation of your trip. For $0 Trip Cost there is no CFAR. <b>This benefit is not available to residents of New York State.</b></p>
  </div>
  <a class="limits-btn" href="#" style="left:96px;top:839px;width:105px;height:12px;font-size:5px">Click here for limitations and exclusions</a>

  <div class="site-footer" style="left:0;top:885px;width:524px;height:18px;display:flex;align-items:center;justify-content:center;gap:4px;font-size:4.3px">
    <span>© 2020 PELLHAM JOURNEYS, INC.</span><span>CONTACT US</span><span>(800) 555-0142</span><span>PRIVACY POLICY</span><span>RESPONSIBILITY</span>
    <span class="seal" style="margin-left:16px;width:38px;height:10px"><i style="width:7px;height:7px"></i><b style="flex:1;height:6px"></b></span>
  </div>

  <div class="reg-head" style="left:322px;top:124px;width:105px;font-size:8.4px"><span>Registration</span><span>Step <span class="step-num">5</span>/8</span></div>
  <div class="tour-info" style="left:322px;top:137px;width:105px;height:56px">
    <div class="tour-info-head" style="font-size:3.9px;padding:3px 4px">YOUR TOUR INFORMATION</div>
    <dl style="font-size:3.8px;line-height:8.6px;padding:3px 4px">
      <div>Group Name: <dd>Maplecrest Elementary School</dd></div>
      <div>Tour Name: <dd>Two Days Test Tour</dd></div>
      <div>Tour Dates: <dd>3/2/2021</dd></div>
      <div>Tour Organizer: <dd>Mr. Alden Testwell</dd></div>
    </dl>
  </div>

  <!-- ================= MOBILE ================= -->
  <div class="view-title" style="left:573px;top:44px">Mobile View</div>
  <div class="brand" style="left:562px;top:74px">
    <span class="brand-mark" style="width:12px;height:12px"></span>
    <span class="brand-name" style="font-size:6.6px">Pellham Journeys</span>
  </div>
  <div class="menu-btn" aria-label="Menu"><span></span><span></span><span></span></div>
  <div class="abs" style="left:559px;top:93px;width:101px;height:1px;background:#eee"></div>

  <div class="reg-head" style="left:562px;top:103px;width:94px;font-size:6.6px"><span>Registration</span><span>Step <span class="step-num">5</span>/8</span></div>
  <div class="tour-info" style="left:562px;top:113px;width:94px;height:43px">
    <div class="tour-info-head" style="font-size:3px;padding:2px 3px">YOUR TOUR INFORMATION</div>
    <dl style="font-size:2.8px;line-height:6.7px;padding:2px 3px">
      <div>Group Name: <dd>Maplecrest Elementary School</dd></div>
      <div>Tour Name: <dd>Two Days Test Tour</dd></div>
      <div>Tour Dates: <dd>3/2/2021</dd></div>
      <div>Tour Organizer: <dd>Mr. Alden Testwell</dd></div>
    </dl>
  </div>

  <div class="abs" style="left:559px;top:160px;width:101px;height:850px;background:var(--panel)"></div>
  <div class="photo" role="img" aria-label="Photo of smiling students taking a selfie in front of the Eiffel Tower" style="left:559px;top:160px;width:101px;height:53px"></div>
  <div class="hero-band" style="left:559px;top:213px;width:101px;height:28px">
    <div class="partner" style="width:27px;justify-content:center;font-size:2.2px"><span class="partner-square" style="width:4px;height:4px"></span>HARBORLINE</div>
    <div style="font-size:3.2px;line-height:4.9px;width:72px">Travel Insurance is optional, but unexpected events are always a possibility… and without the Student Deluxe Group Travel Protection, you might lose up to 100% of your trip investment.</div>
  </div>

  <div class="protect-title" style="left:564px;top:248px;width:92px;font-size:6.4px;line-height:8px">PROTECT YOUR TRIP INVESTMENT!</div>
  <div class="copy" style="left:564px;top:268px;width:92px;font-size:4px;line-height:6.75px">
    <p>Harborline Travel Cover, a leading provider of group travel insurance, offers participants the opportunity to protect their travel investment.</p>
    <p>This program offers an array of <b>travel protection</b> benefits including 24/7 Worldwide Non-Insurance Assistance Services as well as Trip Cancellation, Trip Interruption, Medical Expense, Baggage and Personal Effects, and more travel insurance coverages such as the Cancel for Any Reason (CFAR) option, if eligible.</p>
  </div>
  <div class="trip-cost" style="left:564px;top:360px;width:92px;font-size:5.8px;line-height:7.4px">To start, please enter your total Trip Cost: $______</div>

  <div class="ribbon" style="left:564px;top:383px;width:92px;height:10px;font-size:4.3px;line-height:10px">RECOMMENDED</div>
  <div class="plan m-plan" style="left:564px;top:393px;width:92px;height:126px">
    <div class="plan-title" style="margin-top:11px">STUDENT DELUXE<br>WITH CFAR</div>
    <div class="plan-price"><sup>$</sup>150</div>
    <div class="plan-tag">Protects your trip investment if you need to cancel for any reason***</div>
    <ul class="plan-list">
      <li class="yes">Trip Cancellation coverage provides a 100% refund if you need to cancel for covered reasons</li>
      <li class="yes">Includes additional coverages as per below Schedule</li>
      <li class="yes">Includes Cancel for Any Reason (CFAR)***</li>
      <li class="yes">Covers cancellation due to fear of a pandemic ***</li>
    </ul>
    <a class="select-btn" href="#" style="left:25px;top:121px">SELECT</a>
  </div>
  <a class="pdf-link" href="#" target="_blank" style="left:560px;top:382px;width:12px;height:12px"><span style="font-size:2.6px;padding:0.6px">PDF</span></a>

  <div class="plan m-plan" style="left:564px;top:538px;width:92px;height:131px">
    <div class="plan-title" style="margin-top:10px">STUDENT DELUXE</div>
    <div class="plan-price"><sup>$</sup>100</div>
    <div class="plan-tag">Protects your trip investment for covered reasons only</div>
    <ul class="plan-list">
      <li class="yes">Trip Cancellation coverage provides a 100% refund if you need to cancel for covered reasons</li>
      <li class="yes">Includes additional coverages as per below Schedule</li>
      <li class="no">Does NOT include Cancel for Any Reason (CFAR)***</li>
      <li class="no">No coverage for cancellations due to fear of a pandemic</li>
    </ul>
    <a class="select-btn" href="#" style="left:23px;top:125px">SELECT</a>
  </div>
  <a class="pdf-link" href="#" target="_blank" style="left:564px;top:532px;width:12px;height:12px"><span style="font-size:2.6px;padding:0.6px">PDF</span></a>

  <div class="plan m-plan" style="left:564px;top:684px;width:92px;height:80px">
    <div class="plan-title" style="margin-top:10px">NONE</div>
    <div class="plan-price"><sup>$</sup>0</div>
    <div class="plan-tag">Potentially lose 100% of your tour cost</div>
    <ul class="plan-list"><li class="no">No Payment Protection</li></ul>
    <a class="select-btn" href="#" style="left:23px;top:75px">SELECT</a>
  </div>
  <a class="pdf-link" href="#" target="_blank" style="left:563px;top:679px;width:12px;height:12px"><span style="font-size:2.6px;padding:0.6px">PDF</span></a>

  <div class="abs" style="left:559px;top:778px;width:101px;height:190px;background:var(--white)"></div>
  <div class="benefits m-table" style="left:559px;top:778px;width:101px">
    <div class="b-row b-head" style="height:15px"><span style="width:58px;font-size:6.2px;padding-left:2px;font-weight:500">Benefit</span><span class="b-none" style="width:18px;font-size:3.6px">NONE</span><span style="width:25px;font-size:3.6px;text-align:center">STUDENT DELUXE</span></div>
    <div class="b-row" style="height:17px"><span class="b-label">CANCEL FOR ANY REASON (CFAR)***</span><span class="b-none x-mark">✕</span><span class="b-dlx x-mark" style="padding-left:12px">✕</span></div>
    <div class="b-row" style="height:13px"><span class="b-label">Trip Cancellation**</span><span class="b-none x-mark">✕</span><span class="b-dlx b-val">Trip Cost*</span></div>
    <div class="b-row" style="height:14px"><span class="b-label">Trip Interruption**</span><span class="b-none x-mark">✕</span><span class="b-dlx b-val">150% Trip Cost</span></div>
    <div class="b-row" style="height:13px"><span class="b-label">Travel Delay – 6 Hours</span><span class="b-none x-mark">✕</span><span class="b-dlx b-val">$750 ($150/day)</span></div>
    <div class="b-row" style="height:17px"><span class="b-label">Missed Connection –<br>3 Hours</span><span class="b-none x-mark">✕</span><span class="b-dlx b-val">$500</span></div>
    <div class="b-row" style="height:13px"><span class="b-label">Baggage/Personal Effects</span><span class="b-none x-mark">✕</span><span class="b-dlx b-val">$1,500</span></div>
    <div class="b-row" style="height:13px"><span class="b-label">Baggage Delay – 24 Hours</span><span class="b-none x-mark">✕</span><span class="b-dlx b-val">$300</span></div>
    <div class="b-row" style="height:20px"><span class="b-label">Emergency Medical Evacuation, Medical Repatriation &amp; Return of Remains</span><span class="b-none x-mark">✕</span><span class="b-dlx b-val">$100,000</span></div>
    <div class="b-row" style="height:18px"><span class="b-label">Accident &amp; Sickness Medical Expense</span><span class="b-none x-mark">✕</span><span class="b-dlx b-val">$25,000</span></div>
    <div class="b-row" style="height:17px"><span class="b-label">Non-Medical Emergency Evacuation</span><span class="b-none x-mark">✕</span><span class="b-dlx b-val">$100,000</span></div>
    <div class="b-row" style="height:16px"><span class="b-label">Non-Insurance Worldwide Emergency Assistance Services</span><span class="b-none x-mark">✕</span><span class="b-dlx b-val">Included</span></div>
  </div>
  <div class="scroll-hint"></div>

  <div class="abs" style="left:559px;top:968px;width:101px;height:158px;background:var(--white)"></div>
  <div class="notes" style="left:564px;top:974px;width:92px;font-size:3.5px;line-height:5.3px">
    <p>Coverages may vary and not all coverage is available in all jurisdictions. Totals listed below each coverage are the maximum benefit amount payable.</p>
    <p>* Up to the lesser of the Trip Cost paid or the limit of Coverage for which benefits are requested and the appropriate plan cost has been paid. Maximum limit of $10,000</p>
    <p>** For $0 Trip Cost, there is no Trip Cancellation and Trip Interruption is limited to $500 return air only</p>
    <p>*** CFAR coverage is the lessor of 75% of the nonrefundable trip cost or up to the maximum of $10,000. CFAR is optional and available for purchase on an individual level. Trip cancellation must be 48 hours or more prior to scheduled departure. CFAR must be purchased at the time of plan purchase and with, or before your final payment. CFAR is available if you paid your Travel Supplier for the full cost for all non-refundable trip costs for your trip prior to your cancellation of your trip. For $0 Trip Cost there is no CFAR. <b>This benefit is not available to residents of New York State.</b></p>
  </div>
  <a class="limits-btn" href="#" style="left:570px;top:1111px;width:79px;height:9px;font-size:3.5px">Click here for limitations and exclusions</a>

  <div class="site-footer" style="left:559px;top:1126px;width:101px;height:19px;font-size:2.4px;line-height:3.6px;padding:2px 3px;text-align:center">
    <div>© 2020 PELLHAM JOURNEYS, INC. &nbsp; CONTACT US &nbsp; (800) 555-0142 &nbsp; PRIVACY POLICY &nbsp; RESPONSIBILITY</div>
    <span class="seal" style="position:absolute;left:2px;top:10px;width:28px;height:7px"><i style="width:5px;height:5px"></i><b style="flex:1;height:4px"></b></span>
  </div>

</div>
</body>
</html>
```